Kovri DIGITAL HORIZON learning portal

We beed a flyer design to launch our new DIGITAL HORIZON Learning Portal. The flyer will be used in letter box drops and to give to small business to encourage sales of this new service.

ABOUT US:

We are a small training firm offering world class training solutions in the areas of:

1. Time Management
2. Sales skills
3. Strategic & High performance leadership
4. Sales Management
5. Personal Maximum Achievement.

You can find our website at www.kovri.com.au

ABOUT DIGITAL HORIZON Learning Portal:

We are launching an online learning portal called DIGITAL HORIZON Learning Portal which will allow anyone, anywhere in the world to take our courses online as long as they have access to a PC, smart phone and internet.

Taking an online course with Kovri through our DIGITAL HORIZON Learning Portal will allow students/participants to save over 50% of the normal price of attending a face to face training program.

There are over 80 different individual learning units that can be taken by a student/participant. The participant can choose to take any unit they wish building their own unique learning experience or they can take a full course in one of the subject areas listed above in the about us section.

ADVANTAGES OF USING THE Kovri DIGITAL HORIZON Learning Portal:

* Cost effective, save over 50% by learning online compared to attending a Kovri class room based programme.
* learning can be scheduled around work and family
* Reduces travel time and travel costs
* Students/participants have the option to select learning materials that meets their level of knowledge and interest.
* Complete flexibility to build a personalised learning experience.
* Students/participants can study anywhere they have access to a computer and Internet connection
* Self-paced learning modules allow students/participants to work at their own pace
* Develops knowledge of the Internet and computers skills that will help learners throughout their lives and careers
* Successfully completing online or computer-based courses builds self-knowledge and self-confidence and encourages students to take responsibility for their learning
* Join over 4 million people who have successfully undertaken the training world wide at a time & a place convenient to students/participants.
* pay securely using zentrapay
* learn based on a students/participants personal financial circumstances with individual units priced at $82.50 each (this is Australian dollars & includes GST)

The final design will be one that conveys flexibility of learning, cost effectiveness of the online learning solution. The flyer design can either be folded, single or double sided, A4 or A5 or DL size - whatever works best in the final outcome.

Industry/Entity Type

Small Business

Requirements
Must have
• The flyer must include:

* the "DIGITAL HORIZON Learning portal" logo and the "Kovri logo" and use the Kovri font. Several logos have been provided and the most appropriate ones can be chosen for the design. The font has been provided. (I do have other logo files in different file formats if required to aid designers)

* The flyer must direct people to the Kovri website www.kovri.com.au to pay, enrol and find out other information about the courses.

* The flyer must highlight cost effectiveness of the solution, the world wide popularity of the programs (over 4 million people have completed the programs world wide), flexibility of learning & the diversity of study areas.

Because of price changes in future of courses it would be very beneficial to be able to edit files in future to show new prices if and when that happens.

```html
<!DOCTYPE html>
<html lang="en">
<head>
<meta charset="utf-8">
<title>Kovri – DIGITAL HORIZON Learning Portal flyer</title>
<link rel="stylesheet" href="https://fonts.googleapis.com/css2?family=Arimo:wght@400;700&family=Great+Vibes&display=swap">
<style>
  :root{
    --backdrop:#4b3630;
    --paper:#ffffff;
    --teal:#1d8f8a;
    --teal-light:#c4e3e2;
    --teal-pale:#d9eeed;
    --segment:#7f9e9d;
    --ink:#2b2b2b;
    --ink-soft:#555555;
    --charcoal:#222222;
    --needle:#1f7fd3;
    --badge:#b9c2c6;
  }
  *{box-sizing:border-box;margin:0;padding:0}
  html,body{width:1200px;height:927px;overflow:hidden}
  body{background:var(--backdrop);font-family:"Arimo",Arial,sans-serif;color:var(--ink);position:relative}

  .page{position:absolute;top:67px;width:560px;height:792px;background:var(--paper);overflow:hidden}
  .page--front{left:30px}
  .page--back{left:610px}

  /* front */
  .front-art{position:absolute;inset:0}
  .programs{position:absolute;left:170px;top:520px;width:390px;list-style:none}
  .programs li{height:40px;margin-bottom:9px;background:var(--teal);color:#fff;
    font-family:"Great Vibes",cursive;font-size:24px;line-height:42px;padding:0 12px 0 14px;
    white-space:nowrap;overflow:visible}
  .portal-mark{position:absolute;left:222px;top:70px;width:156px;height:58px;background:var(--charcoal);
    display:flex;align-items:center;justify-content:center;gap:8px;color:#f2f2f2;
    font-family:"Arimo",Arial,sans-serif;font-weight:700;font-size:14px;letter-spacing:.5px}
  .portal-mark .dot{width:10px;height:10px;background:#f2f2f2}

  /* back */
  .top-band{position:absolute;left:0;top:0;width:560px;height:18px;background:var(--teal)}
  .rule{position:absolute;left:30px;top:30px;width:500px;height:13px;border-radius:7px;background:var(--charcoal)}
  .column{position:absolute;top:62px;width:240px;font-size:9.5px;line-height:1.5;color:var(--ink-soft)}
  .column--left{left:30px}
  .column--right{left:290px}
  .column h2{font-size:10px;font-weight:700;color:var(--ink);margin-bottom:6px}
  .column p{margin-bottom:8px}
  .column ul{padding-left:12px}
  .column li{margin-bottom:3px}
  .partners{position:absolute;left:300px;top:250px;width:230px;display:flex;flex-wrap:wrap;gap:10px 14px}
  .partners span{display:block;width:44px;height:16px;background:var(--badge);border-radius:2px}
  .partners span.round{width:18px;border-radius:50%}
  .brand{position:absolute;left:300px;top:310px;display:flex;align-items:center;gap:12px}
  .brand .square{width:52px;height:52px;background:var(--teal)}
  .brand .name{font-size:42px;font-weight:400;color:var(--ink)}
  .contact{position:absolute;left:300px;top:374px;font-size:9.5px;line-height:1.55;color:var(--ink-soft)}
  .contact .web{color:var(--teal);font-weight:700}
  .crowd{position:absolute;left:0;bottom:0;width:560px;height:300px;
    background:linear-gradient(180deg,#ffffff 0%,#c9c9c9 30%,#6d6d6d 70%,#3a3a3a 100%)}
</style>
</head>
<body>

<section class="page page--front" aria-label="Flyer front">
  <svg class="front-art" width="560" height="792" viewBox="0 0 560 792">
    <defs>
      <path id="reach-arc" d="M181.5 282.6 A100 100 0 1 0 378.5 282.6"/>
    </defs>
    <rect x="0" y="0" width="560" height="640" fill="var(--teal-light)"/>
    <path d="M132 246.1 A157.5 157.5 0 1 0 435.1 272.7" fill="none" stroke="var(--segment)" stroke-width="95"
      role="img" aria-label="Ring of photographs showing learners and trainers"/>
    <g stroke="var(--teal-light)" stroke-width="6">
      <line x1="378.5" y1="282.6" x2="491.8" y2="262.6"/>
      <line x1="374" y1="334.2" x2="482.1" y2="373.5"/>
      <line x1="344.3" y1="376.6" x2="418.2" y2="464.7"/>
      <line x1="297.4" y1="398.5" x2="317.4" y2="511.8"/>
      <line x1="245.8" y1="394" x2="206.5" y2="502.1"/>
      <line x1="203.4" y1="364.3" x2="115.3" y2="438.2"/>
      <line x1="181.5" y1="317.4" x2="68.2" y2="337.4"/>
      <line x1="186" y1="265.8" x2="77.9" y2="226.5"/>
    </g>
    <circle cx="280" cy="300" r="110" fill="var(--teal-pale)"/>
    <rect x="200" y="0" width="200" height="250" fill="var(--teal)"/>
    <polygon points="274,302 286,302 306,185" fill="var(--needle)"/>
    <text font-family="Arimo, Arial, sans-serif" font-size="10.5" fill="var(--ink)">
      <textPath href="#reach-arc" startOffset="50%" text-anchor="middle">over 4 million people have completed the programs world wide</textPath>
    </text>
  </svg>
  <div class="portal-mark"><span class="dot"></span>DIGITAL HORIZON</div>
  <ul class="programs">
    <li>Time Management</li>
    <li>Sales skills</li>
    <li>Strategic &amp; High performance leadership</li>
    <li>Sales Management</li>
    <li>Personal Maximum Achievement</li>
  </ul>
</section>

<section class="page page--back" aria-label="Flyer back">
  <div class="top-band"></div>
  <div class="rule"></div>

  <div class="column column--left">
    <h2>ABOUT DIGITAL HORIZON Learning Portal:</h2>
    <p>We are launching an online learning portal called DIGITAL HORIZON Learning Portal which will allow anyone, anywhere in the world to take our courses online as long as they have access to a PC, smart phone and internet.</p>
    <p>Save over 50% of the normal price of attending a face to face training program. Choose from over 80 individual learning units, or take a full course in one subject area.</p>
    <ul>
      <li>Learning scheduled around work and family</li>
      <li>Reduces travel time and travel costs</li>
      <li>Self-paced learning modules</li>
      <li>Pay securely using zentrapay</li>
      <li>Units priced at $82.50 each (AUD incl. GST)</li>
    </ul>
  </div>

  <div class="column column--right">
    <h2>Our Clients</h2>
    <p>Our programs have been delivered to teams in banking, retail, technology, government, health, education, manufacturing and professional services, from small local firms to large national organisations across Australia and the wider region, with results measured in growth and lasting change.</p>
  </div>

  <div class="partners" aria-label="Client badges">
    <span class="round"></span><span></span><span></span><span></span>
    <span></span><span class="round"></span><span></span>
  </div>

  <div class="brand"><span class="square"></span><span class="name">Kovri</span></div>
  <div class="contact">
    Level 3, 18 Harbour Lane, Brisbane QLD 4000<br>
    Phone: +61 7 5550 1842<br>
    hello@kovri.com.au<br>
    <span class="web">www.kovri.com.au</span>
  </div>

  <div class="crowd" role="img" aria-label="Silhouette of a cheering crowd with raised arms"></div>
</section>

</body>
</html>
```